Simple and Clean business card design

We would like the design to be simple clean and to incorporate our colors.

We are open to your design and talent, we have the dots in our logo as we think of it as data points and we connect data points for people.

We are open to see the great creative and clean design you bring to the table

Contact Information for Business Card

please include: name, position, email, phone and website

Font styles to use
Sans Serif

Requirements
Must have
• my colors incorporated, simplicity
Nice to have
• lots of white space, simplicity
Should not have
• complexicity/ complex art

```html
<!DOCTYPE html>
<html lang="en">
<head>
<meta charset="utf-8">
<title>Nectra — Business Card</title>
<link rel="stylesheet" href="https://fonts.googleapis.com/css2?family=Work+Sans:wght@400;500;600&display=swap">
<style>
  :root{
    --backdrop:#b1b1ad;
    --card-white:#ffffff;
    --card-dark:#1c1c1c;
    --brand-blue:#5b7fc7;
    --ink:#151515;
    --ink-soft:#2a2a2a;
    --white:#ffffff;
  }
  *{box-sizing:border-box;margin:0;padding:0}
  html,body{width:1200px;height:801px;overflow:hidden}
  body{
    background:var(--backdrop);
    font-family:"Work Sans",Arial,sans-serif;
    position:relative;
  }
  .card{
    position:absolute;
    top:246px;
    width:540px;
    height:309px;
    border-bottom:4px solid var(--brand-blue);
    box-shadow:0 10px 24px rgba(0,0,0,.18);
    overflow:hidden;
  }
  .card--front{left:40px;background:var(--card-white)}
  .card--back{left:620px;background:var(--card-dark)}

  .front__tab{
    position:absolute;top:72px;right:0;width:8px;height:34px;
    background:var(--brand-blue);
  }
  .wordmark{
    display:flex;align-items:center;gap:10px;
    font-weight:600;letter-spacing:-.5px;
  }
  .wordmark__dot{border-radius:50%;background:var(--brand-blue);flex:none}
  .front__logo{position:absolute;left:34px;top:96px;font-size:52px;color:var(--ink)}
  .front__logo .wordmark__dot{width:14px;height:14px}

  .front__person{position:absolute;right:32px;top:74px;text-align:right}
  .front__name{
    font-size:23px;font-weight:500;letter-spacing:2.5px;
    color:var(--brand-blue);text-transform:uppercase;
  }
  .front__role{font-size:14px;color:var(--ink-soft);margin-top:2px}

  .front__divider{
    position:absolute;left:34px;right:20px;top:174px;
    border-top:1px solid var(--brand-blue);
  }
  .front__contacts{
    position:absolute;left:48px;top:196px;list-style:none;
    font-size:14.5px;color:var(--ink);line-height:1.35;
  }
  .front__contacts li{display:flex;align-items:center;gap:8px}
  .front__contacts svg{width:10px;height:10px;flex:none}
  .front__address{
    position:absolute;right:32px;top:196px;text-align:right;
    font-size:14.5px;color:var(--ink);line-height:1.35;font-style:normal;
  }

  .back__logo{position:absolute;right:48px;bottom:70px;font-size:82px;color:var(--white)}
  .back__logo .wordmark__dot{width:20px;height:20px}
</style>
</head>
<body>
  <section class="card card--front" aria-label="Business card front">
    <span class="front__tab"></span>
    <div class="wordmark front__logo"><span class="wordmark__dot"></span>Nectra</div>
    <div class="front__person">
      <p class="front__name">Daniel Reyes</p>
      <p class="front__role">Founder</p>
    </div>
    <div class="front__divider"></div>
    <ul class="front__contacts">
      <li><svg viewBox="0 0 10 10" aria-hidden="true"><path d="M2 1l2 2-1 1.2c.6 1.2 1.4 2 2.6 2.6L6.8 6 9 8l-1.2 1.4C4.6 9 1 5.4.6 2.2z" fill="var(--brand-blue)"/></svg>0400 128 937</li>
      <li><svg viewBox="0 0 10 10" aria-hidden="true"><rect x=".6" y="2" width="8.8" height="6" fill="none" stroke="var(--brand-blue)" stroke-width="1"/><path d="M.6 2L5 5.6 9.4 2" fill="none" stroke="var(--brand-blue)" stroke-width="1"/></svg>hello@nectrahub.com</li>
      <li><svg viewBox="0 0 10 10" aria-hidden="true"><circle cx="5" cy="5" r="4.2" fill="none" stroke="var(--brand-blue)" stroke-width="1"/><ellipse cx="5" cy="5" rx="1.8" ry="4.2" fill="none" stroke="var(--brand-blue)" stroke-width=".8"/><path d="M.8 5h8.4" stroke="var(--brand-blue)" stroke-width=".8"/></svg>www.nectrahub.com</li>
    </ul>
    <address class="front__address">418 Cedar Grove Lane<br>Marlow, TX 75001</address>
  </section>

  <section class="card card--back" aria-label="Business card back">
    <div class="wordmark back__logo"><span class="wordmark__dot"></span>Nectra</div>
  </section>
</body>
</html>
```